Business Landing Page for SEO Company

Need the landing page of the website designed - I will provide the copy, will need to include details of my company and the services offered, about us, testimonials, faq, etc., and all these elements will need to be arranged graphically on the page.

I want something similar to this: https://pebrovault.com/

Not in terms of color or theme or anything, but we offer a similar service and want to display similar information.

Th services we provide are:

Premium Links
Monthly Links Subscription
Link Insertions

Need to advertise them on the front page. Additionally need a place for testimonials, company details, etc.,

We already have logo for the website. Please use the attached file to insert the logo within the overal design.

Target Market(s)

SEO marketers and agencies

Number of Pages Required

1 page

```html
<!DOCTYPE html>
<html lang="en">
<head>
<meta charset="utf-8">
<title>Linkora – Link Building for SEO Agencies</title>
<link rel="stylesheet" href="https://fonts.googleapis.com/css2?family=Poppins:ital,wght@0,300;0,400;0,500;0,600;0,700;1,400;1,500&family=Varela+Round&display=swap">
<style>
:root{
  --blue:#2c8be0;
  --blue-dark:#1f74c4;
  --orange:#ff8a00;
  --ink:#1c1c1c;
  --text:#5d5d5d;
  --night:#141a22;
  --white:#ffffff;
  --line:#e3e3e3;
}
*{box-sizing:border-box;margin:0;padding:0}
html,body{width:1200px;height:4255px;overflow:hidden}
body{position:relative;font-family:"Poppins",sans-serif;color:var(--text);background:var(--white)}
.abs{position:absolute}
.heading{font-family:"Varela Round",sans-serif;color:var(--ink);font-weight:400}
.btn{position:absolute;display:flex;align-items:center;justify-content:center;background:var(--orange);color:var(--white);font-size:14px;font-weight:500;border-radius:8px;text-transform:uppercase;letter-spacing:.3px}
.center{left:0;width:1200px;text-align:center}

/* top bar + nav */
.topbar{top:0;left:0;width:1200px;height:33px;background:var(--blue);z-index:5;display:flex;justify-content:flex-end;align-items:center;gap:22px;padding-right:62px;color:var(--white);font-size:14px}
.topbar span{display:flex;align-items:center;gap:8px}
.topbar i{width:24px;height:24px;border-radius:50%;background:var(--orange);display:flex;align-items:center;justify-content:center}
.brand{font-family:"Poppins",sans-serif;font-weight:600;font-size:42px;line-height:50px;color:var(--white);letter-spacing:-.5px}
.nav{top:66px;right:62px;display:flex;gap:24px;font-size:13px;color:var(--white);z-index:5}
.nav .active{color:var(--orange);position:relative}
.nav .active:after{content:"";position:absolute;left:50%;bottom:-9px;width:4px;height:4px;margin-left:-2px;border-radius:50%;background:var(--orange)}

/* hero */
.hero-photo{top:0;left:0;width:1200px;height:760px;background:linear-gradient(100deg,#0e1218 0%,#2a2f36 35%,#3a3f45 55%,#1d2229 80%,#4a4f55 100%)}
.hero-title{top:232px;font-size:52px;line-height:66px;color:var(--white);font-family:"Poppins",sans-serif;font-weight:300;letter-spacing:1px}
.hero-title strong{font-weight:700}
.hero-title .b{color:var(--blue)}
.hero-copy{top:375px;left:330px;width:540px;text-align:center;color:#e6e6e6;font-size:12.5px;line-height:21px}
.slide-arrow{width:40px;height:40px;border:1.5px solid #d0d0d0;border-radius:50%;top:272px}

/* services */
.service{width:240px;text-align:center}
.diamond{position:absolute;left:50%;width:80px;height:80px;margin-left:-40px;transform:rotate(45deg);background:var(--white);border:2px solid var(--orange);border-radius:14px;box-shadow:0 4px 14px rgba(0,0,0,.08)}
.diamond .glyph{position:absolute;left:16px;top:16px;width:44px;height:44px;border-radius:50%;background:linear-gradient(135deg,#dbe9f7,#fde1c0);transform:rotate(-45deg)}
.service h3{font-weight:500;font-size:15px;color:var(--ink);line-height:20px}
.service p{font-size:11.5px;line-height:19px;margin-top:12px}

/* about */
.label{font-size:14px;color:var(--blue);letter-spacing:.5px;text-transform:uppercase}
.about-photo{top:1106px;left:299px;width:602px;height:284px;border-radius:14px;background:linear-gradient(110deg,#3b4634 0%,#6b6f63 30%,#c8c7c1 55%,#eeeeec 75%,#f6f6f6 100%)}
.about-copy{top:1423px;left:330px;width:540px;text-align:center;font-size:12px;line-height:21px}
.about-quote{top:1498px;left:345px;width:510px;text-align:center;font-size:13px;line-height:21px;font-style:italic;color:#333;font-weight:500}

/* start */
.start-title{top:1743px;left:157px;font-size:38px;line-height:43px}
.start-copy{top:1843px;left:158px;width:345px;font-size:11.5px;line-height:21px}
.start-art{top:1678px;left:595px;width:400px;height:330px;border-radius:10px;background:radial-gradient(circle at 45% 40%,#ffffff 0%,#eef2f6 55%,rgba(255,255,255,0) 75%)}

/* testimonial */
.testi-label{top:2108px;color:var(--white)}
.testi-title{top:2138px;font-size:36px;color:var(--white)}
.avatar{top:2220px;left:548px;width:100px;height:100px;border-radius:50%;border:4px solid var(--orange);background:linear-gradient(160deg,#f0f0f0,#c9d7e6)}
.quote-badge{top:2222px;left:615px;width:26px;height:26px;border-radius:50%;background:var(--orange);color:var(--white);font-size:22px;line-height:30px;text-align:center;font-family:Georgia,serif}
.testi-copy{top:2350px;left:308px;width:584px;text-align:center;color:var(--white);font-size:12.5px;line-height:23px}
.client{top:2440px;color:var(--white);font-size:14px;letter-spacing:.5px}

/* blog */
.blog{top:2534px;left:0;width:1200px;height:488px;background:linear-gradient(100deg,#1e2630 0%,#2c3540 40%,#1b222b 70%,#262e38 100%)}
.blog-title{top:2602px;font-size:38px;color:var(--white)}
.post{top:2676px;width:270px;height:261px;overflow:hidden}
.post .shot{position:absolute;inset:0}
.post .shade{position:absolute;inset:0;background:linear-gradient(to bottom,rgba(0,0,0,0) 40%,rgba(0,0,0,.75) 100%)}
.post .date{position:absolute;left:16px;top:166px;height:28px;padding:0 12px;background:var(--orange);border-radius:5px;color:var(--white);font-size:12px;display:flex;align-items:center;gap:6px}
.post p{position:absolute;left:18px;top:206px;width:240px;color:var(--white);font-size:13px;line-height:20px}

/* faq */
.faq-title{top:3088px;font-size:38px}
.faq{left:281px;width:638px;height:45px;border:1px solid var(--line);border-radius:6px;display:flex;align-items:center;padding:0 20px 0 10px;font-size:12.5px;color:#222;gap:18px;box-shadow:0 2px 6px rgba(0,0,0,.04)}
.faq .q{width:26px;height:26px;border-radius:50%;background:#111;color:var(--white);display:flex;align-items:center;justify-content:center;font-size:14px;font-weight:600;flex:none}
.faq .t{flex:1}
.faq .s{font-size:22px;font-weight:300;color:#222}
.faq.open{border-color:var(--orange);color:var(--orange)}
.faq.open .q{background:var(--orange)}
.faq.open .s{color:var(--orange)}
.faq-answer{top:3237px;left:281px;width:638px;height:96px;border:1px solid var(--line);border-radius:6px;padding:18px 58px;font-size:11.5px;line-height:19px}

/* contact */
.contact-label{top:3767px;color:var(--white)}
.contact-title{top:3793px;font-size:36px;color:var(--white)}
.field{background:var(--white);height:36px;font-size:11px;color:#666;padding:12px 14px}
.info-title{top:3868px;left:788px;color:var(--white);font-size:16px}
.info-row{left:783px;display:flex;gap:14px;color:var(--white);font-size:14px;align-items:flex-start}
.info-row i{width:30px;height:30px;border-radius:50%;background:var(--orange);display:flex;align-items:center;justify-content:center;flex:none}

/* footer */
.footer{top:4137px;left:0;width:1200px;height:118px;background:var(--night)}
.foot-links{top:4188px;font-size:11.5px;color:#d6d6d6}
.foot-copy{top:4210px;font-size:11px;color:#bbb}
.social{top:4178px;width:32px;height:32px;border:2px solid var(--orange);border-radius:7px}
</style>
</head>
<body>

<!-- Header -->
<div class="abs topbar">
  <span><i><svg width="12" height="12" viewBox="0 0 24 24"><path fill="#fff" d="M6.6 10.8a15 15 0 0 0 6.6 6.6l2.2-2.2c.3-.3.7-.4 1-.2 1.1.4 2.3.6 3.6.6.6 0 1 .4 1 1V20c0 .6-.4 1-1 1A17 17 0 0 1 3 4c0-.6.4-1 1-1h3.5c.6 0 1 .4 1 1 0 1.3.2 2.5.6 3.6.1.3 0 .7-.2 1z"/></svg></i>555 010 2468</span>
  <span><i><svg width="12" height="12" viewBox="0 0 24 24"><rect x="3" y="5" width="18" height="14" rx="2" fill="#fff"/><path d="M3 6l9 7 9-7" fill="none" stroke="#ff8a00" stroke-width="1.8"/></svg></i>info@linkora.com</span>
</div>

<div class="abs hero-photo" role="img" aria-label="Photo of a man working at a computer in a dim office"></div>
<svg class="abs" style="top:0;left:0" width="1200" height="760">
  <path d="M0 712 C120 700 200 620 330 640 C470 660 520 745 640 722 C800 690 920 530 1200 472 L1200 760 L0 760Z" fill="#fff"/>
  <path d="M0 712 C120 700 200 620 330 640 C470 660 520 745 640 722 C800 690 920 530 1200 472" fill="none" stroke="#2c8be0" stroke-width="4"/>
</svg>

<div class="abs brand" style="top:44px;left:58px;z-index:5">linkora</div>
<nav class="abs nav">
  <span class="active">Home</span><span>About</span><span>Services</span><span>Testimonials</span><span>Blog</span><span>Contact Us</span>
</nav>

<div class="abs slide-arrow" style="left:39px"><svg width="37" height="37" viewBox="0 0 37 37"><path d="M21 12l-6 6.5 6 6.5" fill="none" stroke="#fff" stroke-width="1.5"/></svg></div>
<div class="abs slide-arrow" style="left:1121px"><svg width="37" height="37" viewBox="0 0 37 37"><path d="M16 12l6 6.5-6 6.5" fill="none" stroke="#fff" stroke-width="1.5"/></svg></div>

<h1 class="abs center hero-title"><strong class="b">LINKORA</strong> FOR YOUR<br><strong>AGENCY'S</strong> <span class="b">SUCCESS</span></h1>
<p class="abs hero-copy">Lorem Ipsum has been the industry's standard text ever since the when an unknown printer took galley of type and scrambled it to make</p>
<div class="btn" style="top:442px;left:532px;width:136px;height:36px">Contact Us</div>

<!-- Services -->
<section class="abs service" style="top:550px;left:194px">
  <div class="diamond" style="top:0"><div class="glyph" role="img" aria-label="Icon of linked documents"></div></div>
  <h3 style="margin-top:136px">Premium<br>Links</h3>
  <p>Lorem Ipsum has been the indus standard dummy text ever since the 1500s, when an unknown printer took a galley of type.</p>
</section>
<div class="btn" style="top:828px;left:248px;width:130px;height:36px">View Option</div>

<section class="abs service" style="top:601px;left:479px">
  <div class="diamond" style="top:0"><div class="glyph" role="img" aria-label="Icon of a hand tapping a subscription screen"></div></div>
  <h3 style="margin-top:136px">Monthly Links<br>Subscription</h3>
  <p>Lorem Ipsum has been the indus standard dummy text ever since the 1500s, when an unknown printer took a galley of type.</p>
</section>
<div class="btn" style="top:880px;left:535px;width:130px;height:36px">View Option</div>

<section class="abs service" style="top:550px;left:763px">
  <div class="diamond" style="top:0"><div class="glyph" role="img" aria-label="Icon of chain links"></div></div>
  <h3 style="margin-top:136px">Link<br>Insertions</h3>
  <p>Lorem Ipsum has been the indus standard dummy text ever since the 1500s, when an unknown printer took a galley of type.</p>
</section>
<div class="btn" style="top:828px;left:818px;width:130px;height:36px">View Option</div>

<!-- About -->
<div class="abs center label" style="top:997px">About</div>
<h2 class="abs center heading" style="top:1022px;font-size:38px">Linkora</h2>
<svg class="abs" style="top:1150px;left:0" width="1200" height="280">
  <path d="M0 130 C250 60 420 240 700 170 C900 120 1050 40 1200 70 L1200 280 L0 280Z" fill="#eef5fc"/>
</svg>
<div class="abs" style="top:1108px;left:272px;width:20px;height:20px;background:#ffb66a;transform:rotate(20deg);border-radius:3px"></div>
<div class="abs" style="top:1200px;left:868px;width:56px;height:56px;background:#6fa9ea;transform:rotate(30deg);border-radius:6px"></div>
<div class="abs" style="top:1366px;left:206px;width:16px;height:16px;background:#5a9ee6;transform:rotate(25deg);border-radius:2px"></div>
<div class="abs about-photo" role="img" aria-label="Photo of a businessman on the phone beside a desktop computer"></div>
<p class="abs about-copy">Lorem Ipsum has been the industry's standard dummy text ever since the when an unknown printer took a galley of type and scrambled it to make a type specimen book. It has survived not only five centuries, but also the leap into electronic typesetting.</p>
<p class="abs about-quote">Lorem Ipsum has been the industry's standard dummy text ever since the when an unknown printer.</p>
<div class="btn" style="top:1559px;left:532px;width:136px;height:36px">Learn More</div>

<!-- Getting started -->
<h2 class="abs heading start-title">Getting Strated<br>With Us ?</h2>
<p class="abs start-copy">Lorem Ipsum has been the industry's standard dummy text ever since the when an unknown printer took a galley of type and scrambled it to make a type.</p>
<div class="btn" style="top:1921px;left:158px;width:136px;height:36px">Contact Us</div>
<div class="abs start-art" role="img" aria-label="Illustration of a desktop monitor with analytics charts, a magnifying glass and a plant"></div>

<!-- Testimonials -->
<svg class="abs" style="top:1870px;left:0" width="1200" height="664">
  <path d="M0 60 C200 150 400 200 650 175 C900 150 1050 90 1200 60 L1200 664 L0 664Z" fill="#2c8be0"/>
</svg>
<div class="abs center label testi-label">Testimonials</div>
<h2 class="abs center heading testi-title">What Our Client Say</h2>
<div class="abs avatar" role="img" aria-label="Portrait of the client"></div>
<div class="abs quote-badge">“</div>
<svg class="abs" style="top:2360px;left:256px" width="20" height="34"><path d="M16 2L4 17l12 15" fill="none" stroke="#fff" stroke-width="2"/></svg>
<svg class="abs" style="top:2360px;left:924px" width="20" height="34"><path d="M4 2l12 15-12 15" fill="none" stroke="#ff8a00" stroke-width="2"/></svg>
<p class="abs testi-copy">" Lorem Ipsum is simply dummy text of the printing and typesetting industry. Lorem Ipsum has been the industry's standard dummy text ever since the 1500s, when an unknown printer took a galley of type and scrambled it to make a type specimen book. "</p>
<div class="abs center client">- CLIENT NAME</div>

<!-- Blog -->
<div class="abs blog" role="img" aria-label="Dimmed background photo of an analytics dashboard"></div>
<h2 class="abs center heading blog-title">Blog Post</h2>
<article class="abs post" style="left:172px">
  <div class="shot" role="img" aria-label="Photo of hands typing on a laptop showing charts" style="background:linear-gradient(150deg,#e9ecef,#b8bec6 50%,#6d747c)"></div>
  <div class="shade"></div>
  <div class="date"><svg width="12" height="12" viewBox="0 0 12 12"><rect x="1" y="2" width="10" height="9" rx="1" fill="none" stroke="#fff"/><path d="M1 5h10" stroke="#fff"/></svg>15 Jan 2021</div>
  <p>Lorem Ipsum has been the industry standard dummy text ever.</p>
</article>
<article class="abs post" style="left:465px">
  <div class="shot" role="img" aria-label="Photo of a notebook with SEO notes, a plant and coloured pens" style="background:linear-gradient(150deg,#7d8f5a,#d9c9a3 45%,#8a7a5e)"></div>
  <div class="shade"></div>
  <div class="date"><svg width="12" height="12" viewBox="0 0 12 12"><rect x="1" y="2" width="10" height="9" rx="1" fill="none" stroke="#fff"/><path d="M1 5h10" stroke="#fff"/></svg>15 Jan 2021</div>
  <p>Lorem Ipsum has been the industry standard dummy text ever.</p>
</article>
<article class="abs post" style="left:758px">
  <div class="shot" role="img" aria-label="Photo of a performance chart on a whiteboard beside a man" style="background:linear-gradient(150deg,#dfe3e6,#9aa3ab 50%,#4b5259)"></div>
  <div class="shade"></div>
  <div class="date"><svg width="12" height="12" viewBox="0 0 12 12"><rect x="1" y="2" width="10" height="9" rx="1" fill="none" stroke="#fff"/><path d="M1 5h10" stroke="#fff"/></svg>15 Jan 2021</div>
  <p>Lorem Ipsum has been the industry standard dummy text ever.</p>
</article>

<!-- FAQ -->
<h2 class="abs center heading faq-title">Faq's</h2>
<div class="abs faq open" style="top:3180px"><span class="q">?</span><span class="t">Lorem Ipsum Is Simply Text of the Printing And type ?</span><span class="s">—</span></div>
<p class="abs faq-answer">It has survived not only five centuries, but also the leap into electronic typesetting, remaining essentially unchanged. It was popularised in the 1960s with the release of Letraset sheets containing more recently with desktop.</p>
<div class="abs faq" style="top:3342px"><span class="q">?</span><span class="t">Lorem Ipsum Is Simply Text of the Printing And type ?</span><span class="s">+</span></div>
<div class="abs faq" style="top:3396px"><span class="q">?</span><span class="t">Lorem Ipsum Is Simply Text indutry of the Printing And type industry ?</span><span class="s">+</span></div>
<div class="abs faq" style="top:3450px"><span class="q">?</span><span class="t">Lorem Ipsum Is Simply Text of the Printing And type ?</span><span class="s">+</span></div>
<div class="abs faq" style="top:3504px"><span class="q">?</span><span class="t">Lorem Ipsum Is Simply Text of the Printing And type ?</span><span class="s">+</span></div>

<!-- Contact -->
<svg class="abs" style="top:3620px;left:0" width="1200" height="520">
  <defs><linearGradient id="contactBg" x1="0" y1="0" x2="1" y2="1"><stop offset="0" stop-color="#2c8be0"/><stop offset="1" stop-color="#2580d6"/></linearGradient></defs>
  <path d="M0 58 C300 110 700 120 1200 12 L1200 520 L0 520Z" fill="url(#contactBg)"/>
</svg>
<div class="abs center label contact-label">Keep In Touch</div>
<h2 class="abs center heading contact-title">Contact Us</h2>

<div class="abs field" style="top:3880px;left:177px;width:261px">Name *</div>
<div class="abs field" style="top:3928px;left:177px;width:261px">Email *</div>
<div class="abs field" style="top:3977px;left:177px;width:261px">Phone *</div>
<div class="abs field" style="top:3880px;left:450px;width:299px">Services *
  <svg class="abs" style="top:15px;right:14px" width="10" height="6"><path d="M0 0h10L5 6z" fill="#ff8a00"/></svg></div>
<div class="abs field" style="top:3928px;left:450px;width:299px;height:84px">How can We Help ? *</div>
<div class="btn" style="top:4024px;left:177px;width:118px;height:34px;font-size:13px">Submit</div>

<div class="abs info-title">Contact Info</div>
<div class="abs info-row" style="top:3908px">
  <i><svg width="14" height="14" viewBox="0 0 24 24"><path fill="#fff" d="M12 2a7 7 0 0 0-7 7c0 5 7 13 7 13s7-8 7-13a7 7 0 0 0-7-7zm0 9.5A2.5 2.5 0 1 1 12 6.5a2.5 2.5 0 0 1 0 5z"/></svg></i>
  <span style="font-size:11px;line-height:17px">Linkora<br>101 – Lorem ipsum simple text print<br>type setting industry.</span>
</div>
<div class="abs info-row" style="top:3978px;align-items:center">
  <i><svg width="14" height="14" viewBox="0 0 24 24"><path fill="#fff" d="M6.6 10.8a15 15 0 0 0 6.6 6.6l2.2-2.2c.3-.3.7-.4 1-.2 1.1.4 2.3.6 3.6.6.6 0 1 .4 1 1V20c0 .6-.4 1-1 1A17 17 0 0 1 3 4c0-.6.4-1 1-1h3.5c.6 0 1 .4 1 1 0 1.3.2 2.5.6 3.6.1.3 0 .7-.2 1z"/></svg></i>
  <span>+1 555 010 2468</span>
</div>
<div class="abs info-row" style="top:4020px;align-items:center">
  <i><svg width="14" height="14" viewBox="0 0 24 24"><rect x="3" y="5" width="18" height="14" rx="2" fill="#fff"/><path d="M3 6l9 7 9-7" fill="none" stroke="#ff8a00" stroke-width="1.8"/></svg></i>
  <span>info@Linkora.com</span>
</div>

<!-- Footer -->
<footer class="abs footer"></footer>
<div class="abs brand" style="top:4166px;left:58px">linkora</div>
<div class="abs center foot-links">Home &nbsp;|&nbsp; About &nbsp;|&nbsp; Services &nbsp;|&nbsp; Testimonials &nbsp;|&nbsp; Blog &nbsp;|&nbsp; Contact Us</div>
<div class="abs center foot-copy">©<span style="color:var(--orange)">linkora</span> - 2021 All rights reserved.</div>
<div class="abs social" style="left:1028px;background:var(--orange)"></div>
<div class="abs social" style="left:1068px"></div>
<div class="abs social" style="left:1108px"></div>

</body>
</html>
```